Garage Door Sales and Repair Website

Looking for a website theme and home page design for a garage door sales and repair company (Copper Ridge Garage).   We have a new logo and color scheme (attached) and need to update our website to match.  Here is the current site http://www.copperridgegarage.example/
The design should lend it self to being responsive and full screen.
I like this site (http://www.bluefern-site-works.example/) how it has different color blocks and I would like to have a slide show on my home page as well.  4 slides utilizing some of the following concepts Garage Opener, Garage Doors, Springs, Garage Door Repair, Specials, Free Estimate, etc...
Would like color design to match logo / business cards attached.
Call for Free Estimate with phone number should be visible on top of the page as well.

Target Market(s)
Consumers
Industry/Entity Type
Professional Service
Number of Pages Required
1 page
Font styles to use
Other font styles liked:
- Oswald, Open Sans, other similar google web fonts

Requirements
Must have
- 4 slides for home page design
- Free Estimate
- Phone Number

Nice to have
- Call out for online specials

```html
<!DOCTYPE html>
<html lang="en">
<head>
<meta charset="utf-8">
<title>Copper Ridge Garage Doors</title>
<link href="https://fonts.googleapis.com/css2?family=Oswald:wght@400;500&family=Lato:wght@400;700;900&family=Questrial&display=swap" rel="stylesheet">
<style>
:root{
  --navy:#434d73;
  --footer:#4b5579;
  --nav:#2d2d2f;
  --nav-line:#444448;
  --text:#2b2b2b;
  --muted:#555;
  --light:#eef0f4;
  --rule:#d9dce3;
  --white:#fff;
}
*{box-sizing:border-box;margin:0;padding:0}
html,body{width:1200px;height:2442px;overflow:hidden}
body{position:relative;background:var(--white);font-family:'Lato',sans-serif;color:var(--text)}

.site-header{position:absolute;left:0;top:0;width:1200px;height:130px;background:var(--navy)}
.brand{position:absolute;left:122px;top:38px;color:var(--white);font-weight:900;font-size:22px;line-height:27px;letter-spacing:1px;text-align:center;white-space:nowrap}
.award{position:absolute;left:808px;top:14px;width:96px;height:100px;border-radius:50%;background:#cfa23c}
.estimate{position:absolute;left:950px;top:52px;width:190px;color:var(--white);text-align:center;white-space:nowrap}
.estimate small{display:block;font-size:14px;line-height:16px;letter-spacing:.3px}
.estimate strong{display:block;font-family:'Oswald',sans-serif;font-weight:500;font-size:28px;line-height:34px;letter-spacing:1px}

.main-nav{position:absolute;left:0;top:130px;width:1200px;height:48px;background:var(--nav);display:flex}
.main-nav a{display:flex;align-items:center;justify-content:center;color:var(--white);text-decoration:none;font-size:14px;font-weight:700;letter-spacing:.3px;border-right:1px solid var(--nav-line);white-space:nowrap}
.main-nav a.active{background:#dcdcdc;color:#333;border-right:none}
.main-nav .spacer{width:132px}

.hero{position:absolute;left:0;top:178px;width:1200px;height:517px;background:
  linear-gradient(180deg,rgba(255,255,255,.35) 0%,rgba(255,255,255,0) 35%),
  linear-gradient(90deg,#cfc8b2 0%,#e6dfc8 30%,#ddd5bd 60%,#cdbfa2 100%)}
.hero-caption{position:absolute;right:0;top:315px;width:674px;height:119px;background:rgba(30,30,34,.72);color:var(--white);font-family:'Oswald',sans-serif;font-size:35px;line-height:41px;text-align:right;padding:16px 34px 0 0;white-space:nowrap}

.services{position:absolute;left:0;top:742px;width:1200px;height:865px}
.services .divider{position:absolute;left:598px;top:0;width:1px;height:905px;background:var(--rule)}
.card{position:absolute;width:446px;height:403px;border:2px solid #dadbe0;background:var(--white)}
.card .photo{height:277px}
.card .band{position:relative;height:124px;background:var(--navy);overflow:hidden;text-align:center}
.card h2{color:var(--white);font-family:'Questrial',sans-serif;font-weight:400;font-size:31px;padding-top:20px;letter-spacing:.3px;white-space:nowrap}
.card .more{position:absolute;left:50%;bottom:-34px;width:66px;height:66px;margin-left:-33px;border-radius:50%;background:var(--white);color:var(--navy);font-size:28px;line-height:50px}
.c1{left:98px;top:0}.c2{left:654px;top:0}.c3{left:98px;top:463px}.c4{left:654px;top:463px}
.photo-repair{background:linear-gradient(120deg,#3a3a3c 0%,#8c8a86 30%,#e4e4e2 55%,#f2f2f0 100%)}
.photo-openers{background:radial-gradient(ellipse at 55% 55%,#c9c6c6 0%,#e8e8e8 45%,#f4f4f4 100%)}
.photo-doors{background:linear-gradient(180deg,#4a2e1c 0%,#9a6a42 18%,#e9dcc4 40%,#c9b9a0 62%,#3c3a40 85%,#2a2a30 100%)}
.photo-springs{background:linear-gradient(180deg,#eee5dc 0%,#d8cec4 45%,#8f8882 65%,#d9cfc4 100%)}

.welcome{position:absolute;left:54px;top:1677px;width:723px}
.welcome h1{font-size:23px;font-weight:700;letter-spacing:.4px;padding-bottom:16px;border-bottom:1px solid #cfd3dc;white-space:nowrap}
.welcome p{margin-top:14px;font-size:18.5px;line-height:33px;color:var(--text)}
.callout{position:absolute;left:54px;top:1990px;width:723px;height:90px;background:var(--navy);color:var(--white);padding:19px 0 0 20px}
.callout p{font-size:14.5px;font-weight:700;line-height:25px;width:440px}
.call-btn{position:absolute;left:492px;top:24px;width:200px;height:42px;border:2px solid #d0d3dc;border-radius:4px;background:#2f3552;color:var(--white);font-size:16px;font-weight:700;padding:10px 0 0 56px;letter-spacing:.3px;white-space:nowrap}
.call-btn .ico{position:absolute;left:-4px;top:-4px;width:46px;height:46px;border-radius:50%;background:#20243a;border:2px solid #d0d3dc;display:flex;align-items:center;justify-content:center}

.offers{position:absolute;left:809px;top:1677px;width:339px;height:404px;border:1px solid #d6d9e0;background:var(--white);box-shadow:0 4px 8px rgba(0,0,0,.12)}
.offers-head{height:77px;display:flex;align-items:center;padding-left:16px}
.offers-head .ico{width:44px;height:44px;border-radius:50%;background:var(--navy);display:flex;align-items:center;justify-content:center;margin-right:14px}
.offers-head h3{font-size:22px;font-weight:700;letter-spacing:.5px}
.offer{position:relative;height:81px;background:var(--light);border-top:2px solid var(--white);padding:14px 74px 0 18px}
.offer h4{font-size:15px;font-weight:700;letter-spacing:.3px;white-space:nowrap}
.offer p{font-size:13px;line-height:16px;color:var(--muted);margin-top:4px}
.tag{position:absolute;right:12px;top:0;width:40px;height:66px;background:var(--navy);color:var(--white);text-align:center;font-size:14px;font-weight:700;line-height:15px;padding-top:8px;clip-path:polygon(0 0,100% 0,100% 100%,50% 82%,0 100%)}
.tag small{display:block;font-size:10px}

.site-footer{position:absolute;left:0;top:2117px;width:1200px;height:263px;background:var(--footer);color:var(--white)}
.f-col{position:absolute;top:22px}
.f-col h5{font-size:19px;font-weight:700;padding-bottom:10px;border-bottom:1px solid #5e688b;width:220px;letter-spacing:.3px}
.quick{left:54px}
.quick ul{list-style:none;margin-top:14px}
.quick li{font-size:14px;height:37px}
.quick li::before{content:"›";margin-right:8px}
.contact{left:295px}
.contact ul{list-style:none;margin-top:10px}
.contact li{font-size:14px;line-height:21px;display:flex;margin-bottom:14px;white-space:nowrap}
.contact li svg{flex:none;margin:3px 16px 0 0}
.contact li b{font-weight:700}
.vline{position:absolute;top:48px;width:1px;height:190px;background:#5e688b}
.badge-rect{position:absolute;left:632px;top:92px;width:164px;height:62px;background:#1b1b1b;border-radius:6px}
.badge-circle{position:absolute;left:840px;top:86px;width:80px;height:80px;border-radius:50%;background:#4aa3d8}
.foot-brand{position:absolute;left:990px;top:102px;width:170px;color:#7e88a8;font-weight:900;font-size:22px;line-height:27px;text-align:center;letter-spacing:1px;white-space:nowrap}

.bottom-bar{position:absolute;left:0;top:2380px;width:1200px;height:62px;background:#b6bfcd}
.bottom-bar .copy{position:absolute;left:0;top:0;width:800px;height:42px;background:var(--white);clip-path:polygon(0 0,100% 0,96% 100%,0 100%);font-size:13px;padding:13px 0 0 54px}
.bottom-bar .base{position:absolute;left:0;bottom:0;width:1200px;height:20px;background:var(--footer)}
.social{position:absolute;left:928px;top:-6px;display:flex;gap:12px}
.social span{width:42px;height:42px;border-radius:50%;border:2px solid var(--white);box-shadow:0 1px 3px rgba(0,0,0,.3)}
</style>
</head>
<body>

<header class="site-header">
  <div class="brand">COPPER RIDGE<br>GARAGE</div>
  <div class="award" role="img" aria-label="Service award badge"></div>
  <div class="estimate"><small>Call for a FREE Estimate</small><strong>303-555-0142</strong></div>
</header>

<nav class="main-nav">
  <span class="spacer"></span>
  <a class="active" style="width:101px">HOME</a>
  <a style="width:190px">OPENERS</a>
  <a style="width:215px">GARAGE DOORS</a>
  <a style="width:269px">BROKEN SPRINGS</a>
  <a style="width:293px;border-right:none">GARAGE DOOR REPAIR</a>
</nav>

<section class="hero" role="img" aria-label="Slide photo: three technicians installing a new garage door with windows">
  <div class="hero-caption">DENVER'S PREFERRED<br>GARAGE DOOR SALES AND REPAIR COMPANY</div>
</section>

<section class="services">
  <div class="divider"></div>
  <article class="card c1">
    <div class="photo photo-repair" role="img" aria-label="Photo: hands adjusting a garage door torsion spring"></div>
    <div class="band"><h2>Garage Door Repair</h2><span class="more">+</span></div>
  </article>
  <article class="card c2">
    <div class="photo photo-openers" role="img" aria-label="Photo: garage door opener unit with wall keypad and remote"></div>
    <div class="band"><h2>Garage Door Openers</h2><span class="more">+</span></div>
  </article>
  <article class="card c3">
    <div class="photo photo-doors" role="img" aria-label="Photo: modern frosted glass garage doors lit at dusk"></div>
    <div class="band"><h2>New Garage Doors</h2><span class="more">+</span></div>
  </article>
  <article class="card c4">
    <div class="photo photo-springs" role="img" aria-label="Photo: broken garage door spring on a shaft"></div>
    <div class="band"><h2>Broken Springs</h2><span class="more">+</span></div>
  </article>
</section>

<section class="welcome">
  <h1>WELCOME TO COPPER RIDGE GARAGE DOORS</h1>
  <p>Lorem ipsum dolor sit amet, consectetur adipiscing elit. In non placerat ex. Maecenas venenatis eleifend urna non rhoncus. Pellentesque vulputate accumsan nunc ac facilisis. Aliquam facilisis rutrum bibendum. Vestibulum auctor rutrum lorem, eu condimentum augue porta nec. Donec tincidunt, nulla at mattis convallis, dolor ex molestie ligula, nec ornare mi mauris vel libero. Vestibulum eleifend turpis ut auctor vehicula. Suspendisse imperdiet, ex sit amet euismod vehicula, tortor ipsum imperdiet nibh, posuere tincidunt dolor mauris vitae enim.</p>
</section>

<div class="callout">
  <p>Fast – Affordable – Professional – No Additional Charge For Weekends – 24 Hour Emergency Service Available</p>
  <div class="call-btn">
    <span class="ico"><svg width="20" height="20" viewBox="0 0 24 24"><path fill="#fff" d="M6.6 10.8a15.1 15.1 0 0 0 6.6 6.6l2.2-2.2c.3-.3.7-.4 1-.2 1.1.4 2.3.6 3.6.6.6 0 1 .4 1 1V20c0 .6-.4 1-1 1A17 17 0 0 1 3 4c0-.6.4-1 1-1h3.5c.6 0 1 .4 1 1 0 1.3.2 2.5.6 3.6.1.3 0 .7-.2 1z"/></svg></span>
    CALL US TODAY
  </div>
</div>

<aside class="offers">
  <div class="offers-head">
    <span class="ico"><svg width="24" height="22" viewBox="0 0 24 22"><path fill="#fff" d="M2 8h4l10-6v18L6 14H2zM7 15l2 6h3l-2-6z"/><path d="M19 7c2 1.5 2 6.5 0 8" stroke="#fff" stroke-width="2" fill="none"/></svg></span>
    <h3>SPECIAL OFFERS</h3>
  </div>
  <div class="offer"><h4>SPRING REPLACEMENT</h4><p>$60 off Replacement of Two Garage Door Springs</p><span class="tag">$60<small>OFF</small></span></div>
  <div class="offer"><h4>NEW GARAGE DOOR</h4><p>$200 off Purchase and Installation of any Double Door</p><span class="tag">$200<small>OFF</small></span></div>
  <div class="offer"><h4>NEW GARAGE DOOR</h4><p>Purchase and Installation of any Single Door</p><span class="tag">$100<small>OFF</small></span></div>
  <div class="offer"><h4>BEST VALUE</h4><p>Overhaul includes new Springs, Rollers, Cables, Pulleys &amp; Bearings</p><span class="tag">$325<small>OFF</small></span></div>
</aside>

<footer class="site-footer">
  <div class="f-col quick">
    <h5 style="width:180px">Quick Links</h5>
    <ul><li>Home</li><li>Openers</li><li>Garage Doors</li><li>Broken Springs</li><li>Garage Door Repair</li></ul>
  </div>
  <div class="vline" style="left:256px"></div>
  <div class="f-col contact">
    <h5>Contact Details</h5>
    <ul>
      <li><svg width="12" height="16" viewBox="0 0 12 16"><path fill="#fff" d="M6 0a6 6 0 0 0-6 6c0 4.5 6 10 6 10s6-5.5 6-10a6 6 0 0 0-6-6zm0 8.5A2.5 2.5 0 1 1 6 3.5a2.5 2.5 0 0 1 0 5z"/></svg><span><b>Copper Ridge Garage</b><br>Harlow Blvd<br>Denver, CO 80021</span></li>
      <li><svg width="14" height="14" viewBox="0 0 24 24"><path fill="#fff" d="M6.6 10.8a15.1 15.1 0 0 0 6.6 6.6l2.2-2.2c.3-.3.7-.4 1-.2 1.1.4 2.3.6 3.6.6.6 0 1 .4 1 1V20c0 .6-.4 1-1 1A17 17 0 0 1 3 4c0-.6.4-1 1-1h3.5c.6 0 1 .4 1 1 0 1.3.2 2.5.6 3.6.1.3 0 .7-.2 1z"/></svg>303-555-0142</li>
      <li><svg width="14" height="14" viewBox="0 0 14 14"><path fill="#fff" d="M3 0h8v4H3zM0 5h14v6h-3v3H3v-3H0zm4 4v4h6V9z"/></svg>303-555-0142</li>
      <li><svg width="14" height="12" viewBox="0 0 14 12"><path fill="#fff" d="M0 1h14v1L7 7 0 2zm0 2.5l7 5 7-5V11H0z"/></svg>info@copperridgegarage.example</li>
    </ul>
  </div>
  <div class="vline" style="left:591px"></div>
  <div class="badge-rect" role="img" aria-label="Accredited business badge"></div>
  <div class="badge-circle" role="img" aria-label="Consumer review listing badge"></div>
  <div class="vline" style="left:960px"></div>
  <div class="foot-brand">COPPER RIDGE<br>GARAGE</div>
</footer>

<div class="bottom-bar">
  <div class="base"></div>
  <div class="copy">Copyright © 2016 Copper Ridge Garage Doors, All Rights Reserved.</div>
  <div class="social">
    <span style="background:#3b5998"></span>
    <span style="background:#2aa3ef"></span>
    <span style="background:#0e76a8"></span>
    <span style="background:#dc4a38"></span>
  </div>
</div>

</body>
</html>
```